I sell Finches---picture of White Finch Bird----

I raise and sell light color and white Finch - need card to give to Pet shops with my name - Dora Pelkey, address: 271 North Corwen St. Marlow Bay, Ca. 95012 - phone - 555-417-3968. All birds raised and nourished in large outside aviary--very healthy and cared for. Would like card to be shiny red with bold print in Broadway font----purple bold print on red card. Design options open - you know best. Would like a picture or pictures of Finches - light or white in color.

THE WREN KEEPER (LARGE, BOLD BROADWAY PRINT)

```html
<!DOCTYPE html>
<html lang="en">
<head>
<meta charset="utf-8">
<title>The Wren Keeper – Business Card</title>
<link rel="stylesheet" href="https://fonts.googleapis.com/css2?family=Fascinate&family=Fascinate+Inline&family=Days+One&display=swap">
<style>
  :root {
    --card-red: #ec1c24;
    --card-purple: #6a2c90;
    --ink-purple: #6b2d8e;
    --paper-white: #ffffff;
    --bird-light: #f3f1f3;
    --bird-shade: #b9aab6;
    --branch-brown: #6e5a52;
  }
  * { margin: 0; padding: 0; box-sizing: border-box; }
  html, body {
    width: 1200px;
    height: 704px;
    overflow: hidden;
    background: var(--paper-white);
  }
  .card {
    position: relative;
    width: 1200px;
    height: 704px;
    overflow: hidden;
  }
  .card-background {
    position: absolute;
    inset: 0;
  }
  .brand-title {
    position: absolute;
    left: 46px;
    top: 28px;
    font-family: "Fascinate Inline", "Fascinate", fantasy;
    font-size: 106px;
    font-weight: 400;
    line-height: 1;
    letter-spacing: 2px;
    color: var(--ink-purple);
    white-space: nowrap;
  }
  .owner-name {
    position: absolute;
    left: 50px;
    top: 192px;
    font-family: "Fascinate Inline", "Fascinate", fantasy;
    font-size: 64px;
    font-weight: 400;
    line-height: 1;
    letter-spacing: 9px;
    color: var(--ink-purple);
    white-space: nowrap;
  }
  .name-rule {
    position: absolute;
    left: 50px;
    top: 270px;
    width: 590px;
    height: 2px;
    background: var(--paper-white);
  }
  .contact-line {
    position: absolute;
    left: 50px;
    display: flex;
    align-items: center;
    gap: 16px;
    font-family: "Fascinate", fantasy;
    font-size: 44px;
    line-height: 1.12;
    letter-spacing: 4px;
    color: var(--ink-purple);
    text-shadow:
      2px 0 0 var(--paper-white), -2px 0 0 var(--paper-white),
      0 2px 0 var(--paper-white), 0 -2px 0 var(--paper-white),
      2px 2px 0 var(--paper-white), -2px -2px 0 var(--paper-white),
      2px -2px 0 var(--paper-white), -2px 2px 0 var(--paper-white);
    white-space: nowrap;
  }
  .contact-address { top: 294px; align-items: flex-start; }
  .contact-address address { font-style: normal; }
  .contact-phone { top: 410px; letter-spacing: 5px; }
  .contact-icon { flex: none; width: 34px; height: 34px; }
  .contact-address .contact-icon { margin-top: 8px; }
  .selling-points {
    position: absolute;
    left: 44px;
    top: 506px;
    list-style: none;
    font-family: "Days One", sans-serif;
    font-size: 37px;
    line-height: 45px;
    letter-spacing: 5px;
    color: var(--ink-purple);
  }
  .selling-points li {
    position: relative;
    padding-left: 24px;
    margin-bottom: 8px;
    white-space: nowrap;
  }
  .selling-points li::before {
    content: "";
    position: absolute;
    left: 0;
    top: 22px;
    width: 8px;
    height: 8px;
    border-radius: 50%;
    background: var(--ink-purple);
  }
</style>
</head>
<body>
  <div class="card">
    <svg class="card-background" width="1200" height="704" viewBox="0 0 1200 704">
      <defs>
        <linearGradient id="finch-photo-tone" x1="0" y1="0" x2="1" y2="1">
          <stop offset="0" stop-color="#f3f1f3"/>
          <stop offset="0.6" stop-color="#b9aab6"/>
          <stop offset="1" stop-color="#6e5a52"/>
        </linearGradient>
      </defs>
      <rect class="red-field" x="0" y="0" width="1200" height="490" fill="var(--card-red)"/>
      <rect class="white-band" x="0" y="490" width="1200" height="214" fill="var(--paper-white)"/>
      <path class="purple-wave"
            d="M1122 -10 C1132 190 1010 270 925 370 C885 420 880 520 884 714 L1210 714 L1210 -10 Z"
            fill="var(--card-purple)" stroke="var(--paper-white)" stroke-width="14"/>
      <rect class="bottom-rule" x="940" y="696" width="260" height="3" fill="var(--paper-white)"/>
      <rect class="finch-photo" role="img" aria-label="Photo of a white finch perched on a branch"
            x="930" y="250" width="270" height="390" rx="24" fill="url(#finch-photo-tone)"/>
    </svg>

    <h1 class="brand-title">THE WREN KEEPER</h1>
    <h2 class="owner-name">DORA PELKEY</h2>
    <div class="name-rule"></div>

    <div class="contact-line contact-address">
      <svg class="contact-icon" viewBox="0 0 34 34" aria-hidden="true">
        <circle cx="17" cy="17" r="16" fill="var(--ink-purple)" stroke="var(--paper-white)" stroke-width="2"/>
        <path d="M17 7c-4 0-7 3-7 7 0 5 7 13 7 13s7-8 7-13c0-4-3-7-7-7z" fill="var(--paper-white)"/>
        <circle cx="17" cy="14" r="2.6" fill="var(--ink-purple)"/>
      </svg>
      <address>271 North Corwen St.<br>Marlow Bay, Ca. 95012</address>
    </div>

    <div class="contact-line contact-phone">
      <svg class="contact-icon" viewBox="0 0 34 34" aria-hidden="true">
        <circle cx="17" cy="17" r="16" fill="var(--ink-purple)" stroke="var(--paper-white)" stroke-width="2"/>
        <path d="M11 9l4 0 1.5 5-2.5 1.5c1 2.5 2.5 4 5 5l1.5-2.5 5 1.5 0 4c-8 1-15-6-14.5-14.5z" fill="var(--paper-white)"/>
      </svg>
      <span>555-417-3968</span>
    </div>

    <ul class="selling-points">
      <li>All birds raised and nourished<br>in large outside aviary</li>
      <li>very healthy and cared for.</li>
    </ul>
  </div>
</body>
</html>
```